One of a Kind Clean Business Card

We need to design a new business card template for our company. Our company designs and produced merchandising displays. You can see a sample of what we produce on our site www.qorvatfixtures.com. I have uploaded our logo in vector format, as well as a picture of our current business cards. We want a totally different look. We want simple and clean, looking forward to seeing what people create.
Updates

I would like to update the address for Tellur Display Group Inc. 418 N Brindle Ave Arlington Heights, IL 60817 Would also note. No QR codes

Industry/Entity Type

Business

Contact Information for Business Card

Need a 1 sided business card designed.

Font styles to use
Serif

Requirements
Must have
• Easy to view; Clean Design
Nice to have
• Features that promote engineering and creativity
Should not have
• Too much clutter, keep it simple

```html
<!DOCTYPE html>
<html lang="en">
<head>
<meta charset="utf-8">
<title>Tellur Display Group Inc. – Business Card</title>
<link rel="stylesheet" href="https://fonts.googleapis.com/css2?family=Open+Sans:wght@400;600;700&display=swap">
<style>
  :root {
    --backdrop: #d9d9d9;
    --card: #ffffff;
    --brand-red: #931b1e;
    --ink: #1a1a1a;
    --muted: #444444;
    --rule: #1a1a1a;
    --on-red: #ffffff;
  }
  * { margin: 0; padding: 0; box-sizing: border-box; }
  html, body {
    width: 1200px; height: 1200px; overflow: hidden;
    background: var(--backdrop);
    font-family: "Open Sans", Arial, sans-serif;
  }
  .canvas {
    width: 1200px; height: 1200px;
    display: flex; align-items: center; justify-content: center;
  }
  .business-card {
    position: relative;
    width: 1000px; height: 572px;
    background: var(--card);
    box-shadow: 0 10px 30px rgba(0,0,0,0.18);
  }
  .brand {
    position: absolute; top: 88px; left: 0; right: 0;
    display: flex; justify-content: center; align-items: center; gap: 14px;
  }
  .brand-mark {
    width: 26px; height: 26px; border-radius: 50%; background: var(--ink);
  }
  .brand-name {
    font-size: 34px; font-weight: 600; color: var(--ink);
  }
  .person-name {
    position: absolute; top: 205px; left: 0; right: 0; text-align: center;
    font-size: 40px; font-weight: 700; color: var(--brand-red);
    letter-spacing: 0.5px;
  }
  .address {
    position: absolute; top: 280px; left: 0; right: 0; text-align: center;
    font-size: 24px; color: var(--muted); letter-spacing: 1px;
  }
  .rule-line {
    position: absolute; left: 0; right: 0; height: 3px; background: var(--rule);
  }
  .rule-top { top: 350px; }
  .rule-mid { top: 487px; }
  .rule-bottom { top: 540px; }
  .contact-band {
    position: absolute; top: 360px; left: 0; right: 0; height: 120px;
    background: var(--brand-red); color: var(--on-red);
    display: flex; align-items: center; justify-content: center;
    font-size: 24px;
  }
  .contact-col { display: flex; flex-direction: column; gap: 8px; }
  .contact-col.left { align-items: flex-end; padding-right: 24px; }
  .contact-col.right { align-items: flex-start; padding-left: 24px; }
  .contact-divider { width: 2px; height: 76px; background: rgba(255,255,255,0.6); }
  .contact-item { display: flex; align-items: center; gap: 8px; }
  .contact-item svg { width: 20px; height: 20px; fill: none; stroke: var(--on-red); stroke-width: 2; }
  .contact-item svg .solid { fill: var(--on-red); stroke: none; }
</style>
</head>
<body>
<main class="canvas">
  <article class="business-card">
    <header class="brand">
      <span class="brand-mark"></span>
      <span class="brand-name">Tellur Display Group Inc.</span>
    </header>

    <h1 class="person-name">DALE MORROW</h1>
    <p class="address">418 N Brindle Ave, Arlington Heights, IL 60817</p>

    <span class="rule-line rule-top"></span>
    <section class="contact-band">
      <div class="contact-col left">
        <span class="contact-item">312-555-0148
          <svg viewBox="0 0 20 20" aria-hidden="true"><rect x="6" y="2" width="8" height="16" rx="1.5"/><line x1="9" y1="15" x2="11" y2="15"/></svg>
        </span>
        <span class="contact-item">info@qorvatfixtures.com
          <svg viewBox="0 0 20 20" aria-hidden="true"><rect x="2" y="5" width="16" height="11"/><polyline points="2,5 10,11 18,5"/></svg>
        </span>
      </div>
      <span class="contact-divider"></span>
      <div class="contact-col right">
        <span class="contact-item">
          <svg viewBox="0 0 20 20" aria-hidden="true"><path class="solid" d="M2 8c0-3 4-4 8-4s8 1 8 4v1h-4V7.5c-1-.6-2.5-.8-4-.8s-3 .2-4 .8V9H2z"/><rect class="solid" x="5" y="10" width="10" height="7" rx="1"/></svg>
          815-555-0192
        </span>
        <span class="contact-item">
          <svg viewBox="0 0 20 20" aria-hidden="true"><circle cx="10" cy="10" r="8"/><ellipse cx="10" cy="10" rx="3.5" ry="8"/><line x1="2" y1="10" x2="18" y2="10"/></svg>
          www.qorvatfixtures.com
        </span>
      </div>
    </section>
    <span class="rule-line rule-mid"></span>
    <span class="rule-line rule-bottom"></span>
  </article>
</main>
</body>
</html>
```